Business card design needed

I have started a new business called Marlow Auto Electrical, although the words Marlow Auto Electrical will be used on signage and documents I actually want to market the business as MAE. The services I offer are Mobile Auto Electrical, Automotive Air Conditioning and Test And Tag. My business will be targetting the Mining Industry, Civil, Rail, Agricultural and Workshop Testing And Tagging. My auto electrical service ranges from fault finding to new vehicle and mine compliance fit outs. I have a very strong focus on quality workmanship. I will upload the logo I have designed and want to use I am happy for the logo colour to change but the design itself must stay the same. I want the design to have a modern, eye catching, energetic feel. As I am a passionate motorsport fan I am happy for this to also influence the design. I am happy for the front of the card to have only the emblem and logo design and the back to have all the info.

Industry/Entity Type

Electrical

Contact Information for Business Card

MAE Marlow Auto Electrical, Dale Penrick, Auto Electrician, Mobile No 0417263859

Requirements
Must have
• On the business card it is mandatory that the following license numbers are shown:

MVRL38462
VDA L071348
ABN 61 839 204 518

```html
<!DOCTYPE html>
<html lang="en">
<head>
<meta charset="utf-8">
<title>MAE – Marlow Auto Electrical business cards</title>
<link rel="stylesheet" href="https://fonts.googleapis.com/css2?family=Questrial&display=swap">
<style>
  :root {
    --deep-blue: #051640;
    --mid-blue: #0d3a9c;
    --bright-blue: #1f66d6;
    --glow: #9fe3ff;
    --brand-yellow: #f2f719;
    --soft-white: #e9ecef;
    --card-black: #050505;
    --card-red: #d0140c;
    --card-dark-red: #3a0000;
    --name-gold: #c9a227;
    --title-red: #e0301a;
  }
  * { margin: 0; padding: 0; box-sizing: border-box; }
  html, body { width: 1200px; height: 968px; overflow: hidden; }
  body { font-family: "Questrial", sans-serif; }

  .presentation {
    position: relative;
    width: 1200px;
    height: 968px;
    overflow: hidden;
  }
  .backdrop {
    position: absolute;
    inset: 0;
    background:
      radial-gradient(ellipse 420px 520px at 1080px 560px, rgba(159,227,255,0.35), transparent 70%),
      radial-gradient(ellipse 700px 220px at 700px 870px, rgba(159,227,255,0.22), transparent 70%),
      radial-gradient(ellipse 900px 700px at 520px 520px, var(--bright-blue), var(--mid-blue) 55%, var(--deep-blue) 100%);
  }
  .brand-title {
    position: absolute;
    left: 0;
    width: 1200px;
    top: 40px;
    text-align: center;
    color: var(--brand-yellow);
    font-size: 166px;
    font-weight: 400;
    line-height: 1;
    letter-spacing: 2px;
  }
  .brand-subtitle {
    position: absolute;
    left: 0;
    width: 1200px;
    top: 232px;
    text-align: center;
    color: var(--soft-white);
    font-size: 46px;
    letter-spacing: 3px;
    text-shadow: 0 4px 10px rgba(0,0,0,0.5);
  }
  .card {
    position: absolute;
    top: 495px;
    width: 430px;
    height: 250px;
    border-radius: 22px;
    overflow: hidden;
    box-shadow: 6px 10px 14px rgba(0,0,0,0.55);
  }
  .card--front { left: 135px; }
  .card--back { left: 600px; }
  .card-art {
    position: absolute;
    inset: 0;
  }
  .card--front .card-art {
    background: linear-gradient(165deg, var(--card-black) 0%, #1a0303 55%, #7a0a06 100%);
  }
  .card--back .card-art {
    background: linear-gradient(180deg, var(--card-dark-red) 0%, #8e0d08 60%, var(--card-red) 100%);
  }
  .card svg { position: absolute; inset: 0; display: block; }
</style>
</head>
<body>
<main class="presentation">
  <div class="backdrop" role="img" aria-label="Deep blue background with glowing light-blue swirls and sparkles"></div>

  <h1 class="brand-title">MAE</h1>
  <p class="brand-subtitle">MARLOW AUTO ELECTRICAL</p>

  <section class="card card--front" aria-label="Business card front">
    <div class="card-art" role="img" aria-label="Black card background with red motorsport swoosh artwork"></div>
    <svg width="430" height="250" viewBox="0 0 430 250">
      <g font-family="Questrial, sans-serif" text-anchor="middle">
        <text x="305" y="122" font-size="40" fill="var(--brand-yellow)" letter-spacing="1">MAE</text>
        <text x="305" y="145" font-size="13.5" fill="var(--soft-white)">MARLOW AUTO ELECTRICAL</text>
        <text x="305" y="171" font-size="10.5" fill="#ffffff">Mobile Auto Electrical</text>
        <text x="305" y="184" font-size="10.5" fill="#ffffff">Automotive Air Conditioning</text>
        <text x="305" y="197" font-size="10.5" fill="#ffffff">Test And Tag</text>
      </g>
    </svg>
  </section>

  <section class="card card--back" aria-label="Business card back">
    <div class="card-art" role="img" aria-label="Red card background with dark glowing emblem artwork"></div>
    <svg width="430" height="250" viewBox="0 0 430 250">
      <defs>
        <linearGradient id="name-gold" x1="0" y1="0" x2="0" y2="1">
          <stop offset="0" stop-color="#f1d36a"/>
          <stop offset="1" stop-color="#8a6410"/>
        </linearGradient>
      </defs>
      <g font-family="Questrial, sans-serif">
        <text x="128" y="91" font-size="34" fill="var(--brand-yellow)" text-anchor="middle" letter-spacing="1">MAE</text>
        <text x="128" y="112" font-size="12.5" fill="var(--soft-white)" text-anchor="middle">MARLOW AUTO ELECTRICAL</text>
        <text x="405" y="106" font-size="19" fill="url(#name-gold)" text-anchor="end" letter-spacing="0.5">DALE PENRICK</text>
        <text x="405" y="127" font-size="11" fill="var(--title-red)" text-anchor="end">Auto Electrician</text>
        <g font-size="11.5" fill="#ffffff" text-anchor="end">
          <text x="405" y="174">Mobile No 0417263859</text>
          <text x="405" y="190">MVR L38462</text>
          <text x="405" y="207">VDA L071348</text>
          <text x="405" y="225">ABN 61 839 204 518</text>
        </g>
      </g>
    </svg>
  </section>
</main>
</body>
</html>
```